We need a postcard design for a new promotion. We are an Australian online store that sells craft mosaic supplies, mainly tiles. View our website to understand more about our product range, www.brightpebbleworks.com.au and what we are about.

This promotion is designed to be used with mosaic studios / classes, as a referral system. They will give these cards to their students who will use them when placing an order. They will enter the studios / classes name during the checkout process. The studio will then receive a credit which will entitle them to receive mosaic supplies.

Target Market(s)

Women aged between 30-65, interest in art & craft

Industry/Entity Type

Store

Requirements
Must have
• Logo
Phone number: 1300 584 716
Website URL: www.brightpebbleworks.com.au

The following wording:

You Can Help Stock Your Studio...
Simply place any order with The Pebble Works and we will give your studio mosaic supplies, to the value of 10% of your purchase.

Just enter your studios name in the comments box during checkout to ensure your studio receives their supplies.

Studio Name:

```html
<!DOCTYPE html>
<html lang="en">
<head>
<meta charset="UTF-8">
<title>The Pebble Works – Studio Referral Postcard</title>
<link rel="stylesheet" href="https://fonts.googleapis.com/css2?family=Exo+2:wght@300;400&family=Handlee&display=swap">
<style>
  :root {
    --bg: #1c1c1e;
    --card: #ffffff;
    --ink: #2b2b2b;
    --ink-soft: #4a4a4a;
    --accent-red: #c9264c;
    --accent-teal: #1f9aa9;
    --brand-grey: #8d8d8d;
    --panel: rgba(255, 255, 255, 0.92);
    --line: #555555;
  }
  * { box-sizing: border-box; margin: 0; padding: 0; }
  html, body {
    width: 1200px; height: 1200px; overflow: hidden;
    background: var(--bg);
    font-family: "Exo 2", sans-serif;
  }
  .postcard {
    position: absolute;
    left: 300px;
    width: 600px; height: 464px;
    background: var(--card);
    overflow: hidden;
  }
  .postcard--front { top: 110px; }
  .postcard--back  { top: 626px; }

  /* Front */
  .front-photo {
    position: absolute; inset: 0;
    background:
      radial-gradient(ellipse at 88% 22%, #9a5a2e 0 14%, transparent 15%),
      radial-gradient(ellipse at 62% 52%, rgba(200, 51, 44, 0.85) 0 8%, transparent 20%),
      radial-gradient(ellipse at 60% 22%, rgba(63, 154, 85, 0.85) 0 10%, transparent 24%),
      radial-gradient(ellipse at 64% 86%, rgba(58, 140, 200, 0.85) 0 10%, transparent 24%),
      linear-gradient(135deg, #d9d8d6, #ecebea 60%, #cfcfcd);
  }
  .front-panel {
    position: absolute; top: 0; bottom: 0; left: 29px; width: 237px;
    background: var(--panel);
    display: flex; flex-direction: column; align-items: center;
    padding-top: 36px;
  }
  .brand {
    display: flex; align-items: center; gap: 9px;
    white-space: nowrap;
  }
  .brand__square {
    flex: none;
    width: 22px; height: 22px; background: var(--brand-grey);
  }
  .brand__name {
    font-weight: 300; font-size: 22px; color: var(--brand-grey);
    line-height: 1;
  }
  .offer {
    margin-top: 34px;
    font-weight: 300; font-size: 34px; line-height: 1.1;
    color: var(--accent-red);
    letter-spacing: 1px;
  }
  .pitch {
    margin-top: 16px;
    text-align: center;
    font-weight: 300; font-size: 16px; line-height: 1.3;
    color: var(--ink-soft);
  }
  .contact {
    position: absolute; bottom: 20px; left: 0; right: 0;
    text-align: center;
    font-weight: 400; font-size: 14px; line-height: 1.4;
    color: var(--accent-teal);
  }
  .quote {
    position: absolute; right: 30px; bottom: 32px;
    font-family: "Handlee", cursive;
    font-size: 16px; line-height: 1.35; color: #ffffff;
    text-align: right;
  }

  /* Back */
  .back-panel {
    position: absolute; top: 0; bottom: 0; left: 23px; width: 278px;
    background: linear-gradient(160deg, #eef1f4, #e4ecef 50%, #eef0ee);
  }
  .mosaic-band {
    position: absolute; left: 0; right: 0; height: 26px;
    background: linear-gradient(90deg, #d8c23a, #4aa36a 30%, #cc3d3d 55%, #2a8aa0 80%, #d8c23a);
  }
  .mosaic-band--top { top: 0; }
  .mosaic-band--bottom { bottom: 0; }
  .back-content {
    position: absolute; left: 40px; top: 54px; width: 250px;
  }
  .instructions {
    margin-top: 30px;
    font-weight: 400; font-size: 16px; line-height: 1.65;
    color: var(--ink);
  }
  .studio-label {
    margin-top: 18px;
    font-size: 16px; color: var(--ink);
  }
  .address {
    position: absolute; left: 327px; top: 303px; width: 230px;
    font-size: 15px; color: var(--ink);
  }
  .address__to { display: flex; align-items: flex-end; gap: 6px; height: 22px; }
  .address__line { flex: 1; border-bottom: 1px solid var(--line); }
  .address__blank { height: 21px; border-bottom: 1px solid var(--line); }
</style>
</head>
<body>
  <section class="postcard postcard--front">
    <div class="front-photo" role="img" aria-label="Photograph of scattered coloured mosaic tiles, glass gems and tile nippers beside a round wooden mosaic tray"></div>
    <div class="front-panel">
      <div class="brand">
        <span class="brand__square"></span>
        <span class="brand__name">The Pebble Works</span>
      </div>
      <p class="offer">10% OFF</p>
      <p class="pitch">You Can Help Stock<br>Your Studio...<br>Simply place any order<br>with The Pebble Works<br>and we will give<br>your studio<br>mosaic supplies, to the<br>value of 10% of<br>your purchase.</p>
      <p class="contact">www.brightpebbleworks.com.au<br>1300 584 716</p>
    </div>
    <p class="quote">"Creativity is<br>contagious, pass it on"<br>- Clara Whitfield</p>
  </section>

  <section class="postcard postcard--back">
    <div class="back-panel" role="img" aria-label="Soft faded mosaic tile pattern with colourful tile bands at top and bottom">
      <div class="mosaic-band mosaic-band--top"></div>
      <div class="mosaic-band mosaic-band--bottom"></div>
    </div>
    <div class="back-content">
      <div class="brand">
        <span class="brand__square"></span>
        <span class="brand__name">The Pebble Works</span>
      </div>
      <p class="instructions">Just enter<br>your studios name in<br>the comments box<br>during checkout<br>to ensure your studio<br>receives their supplies.</p>
      <p class="studio-label">Studio Name:</p>
    </div>
    <div class="address">
      <div class="address__to"><span>To :</span><span class="address__line"></span></div>
      <div class="address__blank"></div>
      <div class="address__blank"></div>
      <div class="address__blank"></div>
      <div class="address__blank"></div>
      <div class="address__blank"></div>
    </div>
  </section>
</body>
</html>
```